table invoices in a modern format! (make it fun to look at!!)

Our has invoices that are shown to our clients. This is currently done in a normal table view, but its boring to look at and is not modern.
We would like to have a modern look and feel
it should ABSOLUTLY not be in table form.
Cards, graphs, pictures, whatever... should be fun and almost interactive.

the table file is how it current looks like.
the other two files were "ideas" to have a better representation
IT DOES NOT NEED TO LOOK LIKE THAT if you have a better idea please go for it.

secondary objective, the graphs/cards/whatever you design should be interactive, meaning I can "click on it" to pay a bill, or see more info.

Let me know if there are more questions!

```html
<!DOCTYPE html>
<html lang="en">
<head>
<meta charset="UTF-8">
<title>Invoices Overview</title>
<link rel="stylesheet" href="https://fonts.googleapis.com/css2?family=Arimo:wght@400&display=swap">
<style>
  :root {
    --bg: #ffffff;
    --price: #510b30;
    --extra: #ef4440;
    --paid: #ff69c4;
    --grid: #b4b4b4;
    --ink: #000000;
  }
  html, body {
    margin: 0;
    padding: 0;
    overflow: hidden;
    background: var(--bg);
  }
  .invoice-canvas {
    width: 1200px;
    height: 578px;
    position: relative;
    overflow: hidden;
    font-family: "Arimo", Arial, sans-serif;
  }
  .invoice-chart { display: block; width: 1200px; height: 578px; }
  .grid-line { stroke: var(--grid); stroke-width: 1; }
  .axis-label { font-size: 13px; fill: var(--ink); }
  .bar-price { fill: var(--price); }
  .bar-extra { fill: var(--extra); }
  .bar { cursor: pointer; }
  .bar:hover { opacity: .88; }
  .paid-line { fill: none; stroke: var(--paid); stroke-width: 5; stroke-linejoin: round; }
  .paid-point { fill: var(--paid); }
  .legend-swatch-price { fill: var(--price); }
  .legend-swatch-extra { fill: var(--extra); }
  .legend-swatch-paid { fill: var(--paid); }
  .legend-label { font-size: 20px; fill: var(--ink); }
</style>
</head>
<body>
<div class="invoice-canvas">
  <svg class="invoice-chart" viewBox="0 0 1366 658" preserveAspectRatio="none" role="img" aria-label="Monthly invoices: price, extra charges and amount paid">
    <g class="grid">
      <line class="grid-line" x1="431" y1="81" x2="919" y2="81"/>
      <line class="grid-line" x1="431" y1="178.6" x2="919" y2="178.6"/>
      <line class="grid-line" x1="431" y1="276.2" x2="919" y2="276.2"/>
      <line class="grid-line" x1="431" y1="373.8" x2="919" y2="373.8"/>
      <line class="grid-line" x1="431" y1="471.4" x2="919" y2="471.4"/>
      <line class="grid-line" x1="431" y1="569" x2="919" y2="569"/>
    </g>
    <g class="y-axis" text-anchor="end">
      <text class="axis-label" x="428" y="85">1,250</text>
      <text class="axis-label" x="428" y="183">1,000</text>
      <text class="axis-label" x="428" y="280">750</text>
      <text class="axis-label" x="428" y="378">500</text>
      <text class="axis-label" x="428" y="475">250</text>
      <text class="axis-label" x="428" y="573">0</text>
    </g>

    <g class="bars">
      <g class="bar" aria-label="January invoice">
        <rect class="bar-extra" x="431" y="139" width="73" height="44" rx="4"/>
        <rect class="bar-price" x="431" y="178.6" width="73" height="390.4"/>
      </g>
      <g class="bar" aria-label="February invoice">
        <rect class="bar-extra" x="514" y="81" width="73" height="24" rx="4"/>
        <rect class="bar-price" x="514" y="100.5" width="73" height="468.5"/>
      </g>
      <g class="bar" aria-label="March invoice">
        <rect class="bar-price" x="597" y="96" width="73" height="473" rx="4"/>
      </g>
      <g class="bar" aria-label="April invoice">
        <rect class="bar-price" x="680" y="124" width="73" height="445" rx="4"/>
      </g>
      <g class="bar" aria-label="May invoice">
        <rect class="bar-price" x="763" y="190" width="73" height="379" rx="4"/>
      </g>
      <g class="bar" aria-label="June invoice">
        <rect class="bar-extra" x="846" y="213" width="73" height="218" rx="4"/>
        <rect class="bar-price" x="846" y="426" width="73" height="143"/>
      </g>
    </g>

    <g class="paid">
      <polyline class="paid-line" points="472,139 553,178 634,100 716,124 797,190 878,213"/>
      <circle class="paid-point" cx="472" cy="139" r="5"/>
      <circle class="paid-point" cx="553" cy="178" r="5"/>
      <circle class="paid-point" cx="634" cy="100" r="5"/>
      <circle class="paid-point" cx="716" cy="124" r="5"/>
      <circle class="paid-point" cx="797" cy="190" r="5"/>
      <circle class="paid-point" cx="878" cy="213" r="5"/>
    </g>

    <g class="x-axis" text-anchor="middle">
      <text class="axis-label" x="468" y="580">JAN</text>
      <text class="axis-label" x="551" y="580">FEB</text>
      <text class="axis-label" x="634" y="580">MARCH</text>
      <text class="axis-label" x="717" y="580">APRIL</text>
      <text class="axis-label" x="800" y="580">MAY</text>
      <text class="axis-label" x="882" y="580">JUNE</text>
    </g>

    <g class="legend">
      <rect class="legend-swatch-price" x="443" y="611" width="39" height="39"/>
      <text class="legend-label" x="493" y="638">Price</text>
      <rect class="legend-swatch-extra" x="609" y="609" width="39" height="39"/>
      <text class="legend-label" x="656" y="636">Extra</text>
      <rect class="legend-swatch-paid" x="763" y="611" width="39" height="39"/>
      <text class="legend-label" x="820" y="638">Paid</text>
    </g>
  </svg>
</div>
</body>
</html>
```